Vorental d.o.o. needes a web site design

We are a company dealing with automatic doors, industrial doors, roller shutters, access control systems.
We would like to get a design which is clean and neat, and here are some sites which work with similar products. These designs are some we like, but of course, I am looking for a design which is unique. We usually use grey and red colours, which you can see on www.vorental.ba .
The sites we like are:
http://www.plinsta.com/gb/
http://www.bravidosteel.it/eng/
http://morrowpanelgate.com/

You have to understand, that we have 4 different groups of products, which are main groups. I would like if those 4 groups somehow could be in different colours. (Maybe "zenpoq" colours), in order to separate the groups in some way.

Attached you have web site structure.

If any questions, please contact me.
Edvan

Target Market(s)

Bosnian market. Aluminium and PVC doors and window market, Construction companies, Supermarkets-Retail, Gas stations, Banks, Food industry, Heavy industry.

Industry/Entity Type

It Company

Contact Information for Business Card

I have attached our current business card in PDF. I weould like english on one side, bosnian on other side.

Logo Text

Vorental is the name of the company, our core business is automation!

Number of Pages Required

5+ page

Font styles to use
Sans Serif

Colors
ec1f27
0792cd
9bcb3c
ffc214
ffffff

```html
<!DOCTYPE html>
<html lang="en">
<head>
<meta charset="utf-8">
<title>Vorental d.o.o. — Automatic Doors, Industrial Doors, Roller Shutters, Access Control</title>
<link rel="stylesheet" href="https://fonts.googleapis.com/css2?family=Exo+2:ital,wght@0,400;0,600;0,700;1,400;1,600;1,700&family=Lato:wght@400;700&display=swap">
<style>
:root{
  --red:#ec1f27;
  --grey-dark:#3a3a3c;
  --grey-nav:#58595b;
  --grey-mid:#6d6e70;
  --grey-text:#555557;
  --grey-light:#f1f1f1;
  --grey-line:#d9d9d9;
  --white:#ffffff;
  --ink:#2b2b2d;
  --head:"Exo 2",sans-serif;
  --body:"Lato",sans-serif;
}
*{box-sizing:border-box;margin:0;padding:0}
html,body{width:1200px;height:2490px;overflow:hidden}
body{font-family:var(--body);color:var(--grey-text);background:var(--white);position:relative}
.wrap{position:relative;width:1098px;margin:0 auto}

/* header */
.site-header{height:103px;background:linear-gradient(#fdfdfd,#f3f3f3)}
.brand{position:absolute;left:0;top:24px;display:flex;align-items:center;gap:14px}
.brand-square{width:34px;height:34px;background:var(--red)}
.brand-name{font-family:var(--head);font-weight:700;font-size:38px;color:var(--grey-nav)}
.header-contact{position:absolute;right:0;top:18px;text-align:right}
.header-top{display:flex;align-items:center;justify-content:flex-end;gap:10px;font-size:15px;color:var(--ink)}
.header-top .sep{width:1px;height:18px;background:var(--grey-line);margin:0 6px}
.social{display:flex;gap:4px}
.social span{width:22px;height:22px;background:var(--grey-mid);display:block}
.call{margin-top:14px;font-size:26px;color:var(--red)}
.call strong{color:var(--ink);font-weight:400;margin-left:6px}

/* nav */
.main-nav{height:47px;background:var(--grey-nav);position:relative}
.main-nav ul{list-style:none;display:flex;height:47px;align-items:center}
.main-nav li{font-family:var(--head);font-style:italic;font-weight:600;font-size:16px;color:var(--white);margin-right:56px}
.main-nav li.active{background:var(--red);height:47px;line-height:47px;padding:0 14px;margin-right:46px}
.nav-cta{position:absolute;right:0;top:-7px;height:54px;width:215px;background:var(--red);font-family:var(--head);font-style:italic;font-weight:600;font-size:20px;color:var(--white);display:flex;align-items:center;justify-content:center}

/* hero */
.hero{height:468px;position:relative;overflow:hidden}
.hero-photo{position:absolute;inset:0;background:linear-gradient(90deg,#e6e6e6 0%,#d9d9d9 40%,#cfd2d5 56%,#9aa3aa 57%,#b9c3c9 75%,#8f9aa2 100%)}
.hero-caption{position:absolute;left:0;top:204px;width:428px;height:106px;background:var(--red);color:var(--white);padding:10px 0 0 52px}
.hero-caption h1{font-family:var(--head);font-weight:600;font-size:38px;line-height:1.1}
.hero-caption p{font-family:var(--head);font-style:italic;font-size:14px;line-height:1.3;margin-top:6px}
.dots{position:absolute;left:52px;bottom:18px;display:flex;gap:8px}
.dots span{width:11px;height:11px;border-radius:50%;background:#fff}
.dots span.on{background:var(--red)}

/* section titles */
.section-title{font-family:var(--head);font-style:italic;font-weight:600;font-size:32px;color:var(--grey-nav);text-align:center}
.section-title em{color:var(--red);font-style:italic}
.divider{display:flex;align-items:center;justify-content:center;gap:10px;margin:10px auto 0}
.divider i{display:block;height:1px;width:150px;background:var(--grey-line)}
.divider b{display:block;width:60px;height:8px;background:linear-gradient(90deg,var(--grey-nav) 50%,var(--red) 50%)}

/* welcome */
.welcome{height:295px;padding-top:45px;text-align:center;box-shadow:0 6px 10px -6px rgba(0,0,0,.15);position:relative}
.welcome .lead{font-size:28px}
.welcome .brand-inline{font-style:normal;font-weight:700;font-size:34px;color:var(--red);margin-left:8px}
.welcome p{font-size:13.5px;line-height:24px;margin:22px auto 0;width:1098px}
.btn-red{display:inline-block;background:var(--red);color:var(--white);font-family:var(--head);font-style:italic;font-weight:600;font-size:16px;padding:6px 26px;border-radius:4px 0 4px 0}
.welcome .btn-red{margin-top:24px}

/* services */
.services{height:440px;padding-top:50px;text-align:center}
.services > p{font-size:13.5px;margin-top:24px}
.tiles{display:flex;gap:2px;margin-top:24px;height:263px}
.tile{flex:1;position:relative;overflow:hidden}
.tile-photo{position:absolute;inset:0}
.tile-label{position:absolute;left:0;right:0;bottom:0;height:43px;background:var(--red);color:var(--white);font-family:var(--head);font-style:italic;font-weight:600;font-size:19px;line-height:43px}
.tile-detail{position:absolute;inset:0;background:rgba(88,89,91,.88);text-align:left;color:var(--white);padding:14px 22px}
.tile-detail h3{font-family:var(--head);font-style:italic;font-weight:400;font-size:19px}
.tile-detail p{font-size:13px;line-height:21px;margin-top:10px}
.tile-detail ul{list-style:none;margin-top:10px}
.tile-detail li{font-size:13px;line-height:28px;display:flex;align-items:center;gap:8px}
.tile-detail .btn-dark{position:absolute;left:30px;bottom:20px;background:var(--grey-dark);font-family:var(--head);font-style:italic;font-weight:600;font-size:15px;padding:4px 24px;border-radius:4px 0 4px 0}

/* partners */
.partners{height:216px;background:var(--grey-light);display:flex;align-items:center;justify-content:center;gap:95px}
.partner{background:#cfcfd1;width:170px;height:72px}

/* inquiry */
.inquiry{height:211px;position:relative;overflow:hidden}
.inquiry-photo{position:absolute;inset:0;background:linear-gradient(180deg,#4c4d4f,#5e5f61 50%,#545557)}
.inquiry .wrap{padding-top:36px}
.inquiry .section-title{color:var(--white)}
.inquiry .divider b{background:linear-gradient(90deg,#9a9a9c 50%,#cfcfcf 50%)}
.inquiry-form{display:flex;gap:10px;margin-top:32px;align-items:center}
.field{height:32px;background:var(--white);border-radius:3px;font-size:13px;color:var(--grey-text);padding:0 10px;line-height:32px}
.field.name,.field.email{width:278px}
.field.msg{width:385px}
.inquiry-form .btn-red{margin-left:auto;width:120px;text-align:center;font-size:17px}

/* info columns */
.info{height:350px;padding-top:40px}
.info .wrap{display:flex}
.col{position:relative}
.col-why{width:292px}
.col-news{width:342px;margin-left:78px}
.col-cat{width:284px;margin-left:102px}
.col h2{font-family:var(--head);font-style:italic;font-weight:600;font-size:24px;color:var(--grey-nav)}
.col h2 em{color:var(--red);font-style:italic}
.col .mini-div{display:block;width:40px;height:6px;background:linear-gradient(90deg,var(--grey-nav) 50%,var(--red) 50%);margin-top:8px}
.why-list{list-style:none;margin-top:22px}
.why-list li{display:flex;gap:12px;font-size:12.5px;line-height:19px;padding:6px 0 11px;border-bottom:1px dashed var(--grey-line);margin-bottom:12px}
.why-list li svg{flex:none;margin-top:3px}
.news-arrows{position:absolute;right:0;top:2px;font-size:28px;font-weight:700;color:var(--grey-nav);letter-spacing:10px}
.news-list{list-style:none;margin-top:20px}
.news-list li{display:flex;gap:14px;margin-bottom:16px}
.date{flex:none;width:46px;text-align:center;border:1px solid var(--grey-line)}
.date b{display:block;background:var(--red);color:var(--white);font-size:18px;line-height:26px;font-weight:400}
.date span{display:block;font-size:11px;line-height:20px;color:var(--ink)}
.news-list h3{font-size:13.5px;font-weight:700;color:var(--ink)}
.news-list p{font-size:12.5px;line-height:18px}
.catalogue{position:relative;margin-top:20px;height:202px;background:linear-gradient(135deg,#e7e7e7,#bdbdbd 45%,#8a3530 60%,#d6d6d6 75%,#f2f2f2)}
.cat-badge{position:absolute;left:0;bottom:22px;display:flex;align-items:center;gap:6px}
.cat-badge .doc{width:40px;height:40px;background:var(--red)}
.cat-badge .cta{background:var(--red);color:var(--white);font-family:var(--head);font-style:italic;font-weight:600;font-size:14px;line-height:16px;padding:4px 14px 4px 16px}

/* footer */
.site-footer{height:297px;background:linear-gradient(180deg,#4a4b4d,#2e2e30);color:var(--white);position:relative}
.site-footer .wrap{display:flex;padding-top:30px;height:297px}
.foot-col h2{font-family:var(--head);font-style:italic;font-weight:600;font-size:19px}
.f-news{width:295px}
.f-news p{font-size:12.5px;line-height:19px;margin-top:14px;color:#e4e4e4}
.f-input{width:205px;height:32px;border:1px solid #555;background:#1f1f20;margin-top:10px;font-size:12px;color:#777;line-height:30px;padding-left:10px}
.f-news .btn-sub{display:inline-block;background:var(--red);font-size:13px;font-weight:700;padding:4px 10px;margin-top:14px;border-radius:2px}
.f-links{width:500px;padding-left:68px;position:relative}
.link-cols{display:flex;gap:40px;margin-top:16px}
.link-cols ul{list-style:none}
.link-cols li{font-size:12.5px;line-height:28px}
.link-cols li::before{content:"› "}
.contact-box{position:absolute;left:58px;top:170px;width:345px;height:62px;background:#1e1e1f;border:1px solid #444;border-radius:4px;display:flex;align-items:center;padding:0 18px;gap:16px}
.contact-box .lbl{color:var(--red);font-size:16px}
.contact-box .num{font-size:24px;color:var(--white)}
.f-loc{margin-left:auto;width:240px}
.map{position:relative;margin-top:14px;height:180px;background:linear-gradient(135deg,#dfe9d6,#eef1ea 40%,#cfdde6 70%,#e6ece0)}
.map-card{position:absolute;left:72px;top:36px;width:118px;background:var(--white);color:var(--ink);font-size:12.5px;line-height:18px;padding:8px 10px;box-shadow:0 2px 6px rgba(0,0,0,.3)}

/* bottom bar */
.bottom-bar{height:63px;background:#202021;color:#d8d8d8;position:relative}
.bottom-bar .wrap{display:flex;align-items:center;height:63px}
.copyright{position:absolute;left:0;right:0;text-align:center;font-size:12.5px}
.foot-brand{margin-left:auto;font-family:var(--head);font-weight:700;font-size:26px;color:var(--red)}
</style>
</head>
<body>

<header class="site-header">
  <div class="wrap">
    <div class="brand"><span class="brand-square"></span><span class="brand-name">Vorental d.o.o.</span></div>
    <div class="header-contact">
      <div class="header-top">
        <svg width="16" height="12" viewBox="0 0 16 12" aria-hidden="true"><rect x="0.5" y="0.5" width="15" height="11" fill="none" stroke="#ec1f27"/><path d="M1 1l7 6 7-6" fill="none" stroke="#ec1f27"/></svg>
        <span>info@vorental.ba</span><span class="sep"></span><span>Follow Us:</span>
        <span class="social"><span></span><span></span><span></span></span>
      </div>
      <div class="call">CALL US TODAY : <strong>033/514-260</strong></div>
    </div>
  </div>
</header>

<nav class="main-nav">
  <div class="wrap">
    <ul>
      <li class="active">Home</li><li>Industrijska Vrata</li><li>Rolo Vrata</li><li>Kontrola Pristupa</li><li>Reference</li><li>Contact</li>
    </ul>
    <div class="nav-cta">Redizajn Stranice</div>
  </div>
</nav>

<section class="hero">
  <div class="hero-photo" role="img" aria-label="Businesswoman using a wall-mounted access control terminal in a glass office building"></div>
  <div class="hero-caption">
    <h1>nova web stranica</h1>
    <p>u toku su radovi na novoj web prezentaciji naših usluga,<br>uskoro smo ponovo sa vama</p>
  </div>
  <div class="dots"><span class="on"></span><span></span><span></span></div>
</section>

<section class="welcome">
  <h2 class="section-title"><span class="lead">Welcome to</span><span class="brand-inline">Vorental d.o.o.</span></h2>
  <div class="divider"><b></b></div>
  <p>Lorem ipsum dolor sit amet, consectetuer adipiscing elit, sed diam nonummy nibh euismod tincidunt ut laoreet dolore magna aliquam erat volutpat. Ut wisi enim ad minim veniam, quis nostrud exerci tation ullamcorper suscipit lobortis nisl ut aliquip ex ea commodo consequat. Duis autem vel eum iriure dolor in hendrerit in vulputate velit esse molestie consequat, vel illum dolore eu feugiat nulla facilisis at vero eros et accumsan et iusto Ut wisi enim ad minim veniam,</p>
  <span class="btn-red">Read More</span>
</section>

<section class="services">
  <h2 class="section-title">We Are <em>C</em>ompany <em>D</em>ealing <em>W</em>ith</h2>
  <div class="divider"><i></i><b></b><i></i></div>
  <p>Lorem ipsum dolor sit amet, consectetuer adipiscing elit, sed diam nonummy nibh euismod tincidunt ut laoreet dolore</p>
  <div class="tiles">
    <div class="tile">
      <div class="tile-photo" role="img" aria-label="Glass automatic sliding doors at a building entrance" style="background:linear-gradient(135deg,#d8dcdf,#aeb6bb 50%,#e9ecee)"></div>
      <div class="tile-label">Automatic Doors</div>
    </div>
    <div class="tile">
      <div class="tile-photo" role="img" aria-label="Industrial hall with sectional doors" style="background:linear-gradient(135deg,#9ea3a7,#7d8387)"></div>
      <div class="tile-detail">
        <h3>Industrial Doors</h3>
        <p>Lorem ipsum dolor sit amet, consectetuer adipiscing elit, sed diam nonummy</p>
        <ul>
          <li><svg width="12" height="12" viewBox="0 0 12 12" aria-hidden="true"><path d="M6 0v12M0 6h12" stroke="#ec1f27" stroke-width="2"/></svg>Lorem ipsum dolor sit amet</li>
          <li><svg width="12" height="12" viewBox="0 0 12 12" aria-hidden="true"><path d="M6 0v12M0 6h12" stroke="#ec1f27" stroke-width="2"/></svg>Lorem ipsum dolor sit amet</li>
          <li><svg width="12" height="12" viewBox="0 0 12 12" aria-hidden="true"><path d="M6 0v12M0 6h12" stroke="#ec1f27" stroke-width="2"/></svg>Lorem ipsum dolor sit amet</li>
        </ul>
        <span class="btn-dark">View All</span>
      </div>
    </div>
    <div class="tile">
      <div class="tile-photo" role="img" aria-label="Row of metal roller shutters in a warehouse" style="background:linear-gradient(180deg,#c7cbce,#8e9599 60%,#b3b8bb)"></div>
      <div class="tile-label">Roller Shutters</div>
    </div>
    <div class="tile">
      <div class="tile-photo" role="img" aria-label="Employee holding a badge to a wall card reader" style="background:linear-gradient(90deg,#7a6a5c,#c9c0b3 55%,#e3ddd3)"></div>
      <div class="tile-label">Access Control Systems</div>
    </div>
  </div>
</section>

<section class="partners" aria-label="Partners">
  <div class="partner"></div>
  <div class="partner"></div>
  <div class="partner"></div>
</section>

<section class="inquiry">
  <div class="inquiry-photo" role="img" aria-label="Dimmed modern office building facade"></div>
  <div class="wrap">
    <h2 class="section-title">Quick Inquiry</h2>
    <div class="divider"><b></b></div>
    <div class="inquiry-form">
      <div class="field name">Name</div>
      <div class="field email">Email</div>
      <div class="field msg">Message</div>
      <span class="btn-red">Submit</span>
    </div>
  </div>
</section>

<section class="info">
  <div class="wrap">
    <div class="col col-why">
      <h2><em>W</em>hy <em>C</em>hoose <em>U</em>s</h2>
      <span class="mini-div"></span>
      <ul class="why-list">
        <li><svg width="12" height="12" viewBox="0 0 12 12" aria-hidden="true"><path d="M6 0v12M0 6h12" stroke="#ec1f27" stroke-width="2"/></svg>Lorem ipsum dolor sit tetu adipiscing elised diam nonummy nibh euismod</li>
        <li><svg width="12" height="12" viewBox="0 0 12 12" aria-hidden="true"><path d="M6 0v12M0 6h12" stroke="#ec1f27" stroke-width="2"/></svg>Lorem ipsum dolor sit tetu adipiscing elised diam nonummy nibh euismod</li>
        <li><svg width="12" height="12" viewBox="0 0 12 12" aria-hidden="true"><path d="M6 0v12M0 6h12" stroke="#ec1f27" stroke-width="2"/></svg>Lorem ipsum dolor sit tetu adipiscing el.</li>
        <li><svg width="12" height="12" viewBox="0 0 12 12" aria-hidden="true"><path d="M6 0v12M0 6h12" stroke="#ec1f27" stroke-width="2"/></svg>Ktu adipiscing elitsied orem ipsum dolo.</li>
      </ul>
    </div>
    <div class="col col-news">
      <h2><em>L</em>atest <em>N</em>ews</h2>
      <span class="mini-div"></span>
      <span class="news-arrows">‹›</span>
      <ul class="news-list">
        <li><div class="date"><b>01</b><span>MAR</span></div><div><h3>Lorem ipsum dolor sitak ametn sit almet</h3><p>Lorem ipsum dolor sitak amet, co<br>adipiscing elit, euismod poor.</p></div></li>
        <li><div class="date"><b>03</b><span>MAR</span></div><div><h3>Lorem ipsum dolor sitak ametn sit almet</h3><p>Lorem ipsum dolor sitak amet, co<br>adipiscing elit, euismod poor.</p></div></li>
        <li><div class="date"><b>07</b><span>MAR</span></div><div><h3>Lorem ipsum dolor sitak ametn sit almet</h3><p>Lorem ipsum dolor sitak amet, co<br>adipiscing elit, euismod poor.</p></div></li>
      </ul>
    </div>
    <div class="col col-cat">
      <h2><em>O</em>ur catalogue</h2>
      <span class="mini-div"></span>
      <div class="catalogue" role="img" aria-label="Automatic glass door entrance featured on the catalogue cover">
        <div class="cat-badge"><span class="doc"></span><span class="cta">Download<br>Our catalogue</span></div>
      </div>
    </div>
  </div>
</section>

<footer class="site-footer">
  <div class="wrap">
    <div class="foot-col f-news">
      <h2>Newsletter Signup</h2>
      <p>Lorem ipsum dolor sit amet,<br>consectetu er adipiscing elit, sed</p>
      <div class="f-input">Name</div>
      <div class="f-input">Email</div>
      <span class="btn-sub">Subscribe</span>
    </div>
    <div class="foot-col f-links">
      <h2>Quick Links</h2>
      <div class="link-cols">
        <ul><li>Home</li><li>Industrijska Vrata</li><li>Rolo Vrata</li><li>Kontrola Pristupa</li></ul>
        <ul><li>Reference</li><li>Contact</li></ul>
      </div>
      <div class="contact-box">
        <span class="lbl">CONTACT US</span>
        <svg width="26" height="26" viewBox="0 0 26 26" aria-hidden="true"><rect width="26" height="26" rx="4" fill="#555"/><path d="M8 6c-2 2 0 8 4 12s9 5 10 3l-3-3-2 2c-2-1-5-4-6-6l2-2z" fill="#ddd"/></svg>
        <span class="num">061/382-447</span>
      </div>
    </div>
    <div class="foot-col f-loc">
      <h2>Our Location</h2>
      <div class="map" role="img" aria-label="Street map showing the office location">
        <svg style="position:absolute;left:42px;top:46px" width="16" height="22" viewBox="0 0 16 22" aria-hidden="true"><path d="M8 0a8 8 0 0 0-8 8c0 6 8 14 8 14s8-8 8-14a8 8 0 0 0-8-8z" fill="#ec1f27"/><circle cx="8" cy="8" r="3" fill="#fff"/></svg>
        <div class="map-card">67 Lorem ipsum Street WA 6065, adipisimg amet</div>
      </div>
    </div>
  </div>
</footer>

<div class="bottom-bar">
  <div class="wrap">
    <span class="social"><span></span><span></span><span></span></span>
    <span class="copyright">Copyright 2016 Vorental d.o.o.. &nbsp;|&nbsp; All Rights Reserved</span>
    <span class="foot-brand">Vorental d.o.o.</span>
  </div>
</div>

</body>
</html>
```